Property Developer - Simple yet Sophisticated and Sharp Business Card

We are a medium sized property developer involved mainly in townhouse developments and land subdivisions.

The company is looking for a simple, sharp and sophisticated business card that will be given to contractors, land owners, financiers etc and thus will need to look professional.

Property development related graphics and art can be used, however the card is not to be too "busy" or crowded. Our company name is KL Estates which could possibly be incorporated into the graphics or artwork.

Single sided and/or double sided designs will be acceptable.

A Simple, Sophisticated, Sharp design please!

Good Luck !

```html
<!DOCTYPE html>
<html lang="en">
<head>
<meta charset="utf-8">
<title>KL Estates – Business Card Concepts</title>
<link rel="stylesheet" href="https://fonts.googleapis.com/css2?family=Arimo:ital,wght@0,400;0,700;1,400&display=swap">
<style>
:root{
  --page:#e2dfd8;
  --card:#f1f1f1;
  --card-edge:#9a9a9a;
  --ink:#1e1e1e;
  --sky:#3fcdf5;
  --sky-soft:#bfeefc;
}
*{margin:0;padding:0;box-sizing:border-box}
html,body{width:1200px;height:856px;overflow:hidden}
body{background:var(--page);font-family:"Arimo",Arial,sans-serif;color:var(--ink);position:relative}
.card{position:absolute;background:var(--card);border:1px solid var(--card-edge);overflow:hidden}
.card--vertical{border-color:#333}
.card > *{position:absolute}
.brand{display:flex;flex-direction:column;align-items:center;justify-content:center;width:130px;height:130px;margin:-65px 0 0 -65px}
.brand__disc{width:110px;height:110px;border-radius:50%;background:var(--sky-soft)}
.brand__name{position:absolute;font-size:19px;font-weight:700;color:var(--ink);white-space:nowrap}
.title{text-align:center;width:140px;margin-left:-70px}
.title__name{font-size:12px;line-height:14px}
.title__role{font-size:9px;line-height:13px;font-style:italic;color:var(--sky)}
.title__rule{height:1px;background:var(--sky);margin-top:2px}
.contacts{font-size:9.5px;line-height:14.5px;white-space:nowrap}
.contacts--right{text-align:right}
.contacts--center{text-align:center;width:100%;left:0;line-height:19.5px}
.swoosh{left:0;width:100%}
.swoosh path.band{fill:var(--sky)}
.swoosh path.trace{fill:none;stroke:var(--sky);stroke-width:1.2}
.icon-row{display:flex;align-items:center;gap:6px;font-size:9.5px;height:20px;white-space:nowrap}
.icon{width:10px;height:10px;fill:var(--ink);flex:none}
</style>
</head>
<body>

<!-- Landscape, logo left -->
<section class="card" style="left:36px;top:93px;width:371px;height:255px">
  <div class="brand" style="left:88px;top:90px"><div class="brand__disc"></div><span class="brand__name">KL Estates</span></div>
  <div class="title" style="left:295px;top:31px"><p class="title__name">Project Owner</p><p class="title__role">Company Director</p><div class="title__rule"></div></div>
  <div class="contacts contacts--right" style="right:2px;top:152px">
    <p>Phone: (07) 3000 1234</p><p>Fax: (07) 3000 5678</p><p>E-mail: projects.klestates@mailbox.com</p><p>Address: PO Box 210 Greenfield QLD 4000</p>
  </div>
  <svg class="swoosh" style="top:210px" width="371" height="45" viewBox="0 0 371 45"><path class="band" d="M0 38 C110 18 260 8 371 6 C260 14 120 30 0 42Z"/><path class="trace" d="M0 45 L371 14"/></svg>
</section>

<!-- Portrait -->
<section class="card card--vertical" style="left:486px;top:196px;width:256px;height:372px">
  <div class="brand" style="left:131px;top:87px"><div class="brand__disc"></div><span class="brand__name">KL Estates</span></div>
  <div class="title" style="left:130px;top:185px"><p class="title__name">Project Owner</p><p class="title__role">Company Director</p><div class="title__rule"></div></div>
  <div class="contacts contacts--center" style="top:256px">
    <p>Tel: (07) 3000 1234</p><p>Fax: (07) 3000 5678</p><p>E-mail: projects.klestates@mailbox.com</p><p>Address: PO Box 210 Greenfield QLD 4000</p>
  </div>
  <svg class="swoosh" style="top:334px" width="256" height="38" viewBox="0 0 256 38"><path class="band" d="M0 32 C80 16 180 7 256 5 C180 12 90 24 0 35Z"/><path class="trace" d="M0 36 L256 10"/></svg>
</section>

<!-- Landscape, contacts top left -->
<section class="card" style="left:793px;top:33px;width:373px;height:257px">
  <div class="contacts" style="left:12px;top:20px">
    <div class="icon-row"><svg class="icon" viewBox="0 0 10 10"><circle cx="5" cy="5" r="4" fill="none" stroke="#1e1e1e" stroke-width="1.4"/><circle cx="5" cy="5" r="1.6"/></svg>projects.klestates@mailbox.com</div>
    <div class="icon-row"><svg class="icon" viewBox="0 0 10 10"><rect x="0" y="1.5" width="10" height="7"/><path d="M0.6 2.2 L5 5.8 L9.4 2.2" fill="none" stroke="#f1f1f1" stroke-width="1"/></svg>PO Box 210 Greenfield QLD 4000</div>
    <div class="icon-row" style="margin-top:4px"><svg class="icon" viewBox="0 0 10 10"><path d="M2 0.5 L3.8 2.8 L2.8 4 Q4 6.2 6 7.2 L7.2 6.2 L9.5 8 L8 9.6 Q3 9 0.4 2Z"/></svg>(07) 3000 1234</div>
    <div class="icon-row"><svg class="icon" viewBox="0 0 10 10"><rect x="2.5" y="0.5" width="5" height="3"/><rect x="0.5" y="4" width="9" height="5.5"/></svg>(07) 3000 5678</div>
  </div>
  <div class="brand" style="left:287px;top:84px"><div class="brand__disc"></div><span class="brand__name">KL Estates</span></div>
  <div class="title" style="left:291px;top:175px"><p class="title__name">Project Owner</p><p class="title__role">Company Director</p><div class="title__rule"></div></div>
  <svg class="swoosh" style="top:215px" width="373" height="42" viewBox="0 0 373 42"><path class="band" d="M0 36 C110 18 260 10 373 8 C260 16 120 30 0 40Z"/><path class="trace" d="M0 42 L373 14"/></svg>
</section>

<!-- Landscape, logo right -->
<section class="card" style="left:87px;top:530px;width:372px;height:256px">
  <div class="brand" style="left:288px;top:84px"><div class="brand__disc"></div><span class="brand__name">KL Estates</span></div>
  <div class="title" style="left:115px;top:125px"><p class="title__name">Project Owner</p><p class="title__role">Company Director</p><div class="title__rule" style="margin:2px 20px 0 -10px"></div></div>
  <svg class="swoosh" style="top:165px" width="372" height="40" viewBox="0 0 372 40"><path class="band" d="M0 30 C120 14 260 6 372 6 C260 16 130 30 0 36Z"/><path class="trace" d="M0 40 L372 12"/></svg>
  <div class="contacts contacts--right" style="right:14px;top:191px">
    <p>Phone: (07) 3000 1234</p><p>Fax: (07) 3000 5678</p><p>E-mail: projects.klestates@mailbox.com</p><p>Address: PO Box 210 Greenfield QLD 4000</p>
  </div>
</section>

<!-- Landscape, icon contacts bottom -->
<section class="card" style="left:761px;top:484px;width:372px;height:256px">
  <div class="brand" style="left:284px;top:86px"><div class="brand__disc"></div><span class="brand__name">KL Estates</span></div>
  <div class="title" style="left:115px;top:118px"><p class="title__name">Project Owner</p><p class="title__role">Company Director</p><div class="title__rule" style="margin:2px -25px 0 -15px"></div></div>
  <svg class="swoosh" style="top:165px" width="372" height="40" viewBox="0 0 372 40"><path class="band" d="M0 30 C120 14 260 5 372 4 C260 14 130 28 0 34Z"/><path class="trace" d="M0 37 L372 8"/></svg>
  <div class="contacts" style="left:35px;top:200px">
    <div class="icon-row"><svg class="icon" viewBox="0 0 10 10"><path d="M2 0.5 L3.8 2.8 L2.8 4 Q4 6.2 6 7.2 L7.2 6.2 L9.5 8 L8 9.6 Q3 9 0.4 2Z"/></svg>(07) 3000 1234</div>
    <div class="icon-row"><svg class="icon" viewBox="0 0 10 10"><rect x="2.5" y="0.5" width="5" height="3"/><rect x="0.5" y="4" width="9" height="5.5"/></svg>(07) 3000 5678</div>
  </div>
  <div class="contacts" style="left:160px;top:200px">
    <div class="icon-row"><svg class="icon" viewBox="0 0 10 10"><circle cx="5" cy="5" r="4" fill="none" stroke="#1e1e1e" stroke-width="1.4"/><circle cx="5" cy="5" r="1.6"/></svg>projects.klestates@mailbox.com</div>
    <div class="icon-row"><svg class="icon" viewBox="0 0 10 10"><rect x="0" y="1.5" width="10" height="7"/><path d="M0.6 2.2 L5 5.8 L9.4 2.2" fill="none" stroke="#f1f1f1" stroke-width="1"/></svg>PO Box 210 Greenfield QLD 4000</div>
  </div>
</section>

</body>
</html>
```